Polystyrene Recycling Material Flow

We need a diagram styled as an infographic that shows how polystyrene foam is recycled starting with a manufactured product, moving through the distribution process, waste material collection and reincorporation back into manufacturing. This is accomplished in different ways once the material is collected which needs to be clearly evident. The most important thing is for it to be simple enough to understand while still having a stylish look. The design can be with or without vector images or photography to depict the different stages. We are providing a very rudimentary 'sketch' of the information points and movement flow. Please see www.foamtradeguild.org (resources) to view our literature branding. The RGB & CMYK are attached.

Target Market(s)

Government Agencies, Brand Owners, Retailers, Recycling Industry

Industry/Entity Type

Packaging, Recycling, Manufacturing

Font styles to use
Sans Serif

Requirements
Must have
• Easy to Understand
Nice to have
• Images - either photography or vector illustrations - are optional. We have provided examples of both to show what could be used but are not required. Substituting your own interpretation of imagery is encouraged.
Should not have
• Outdated look.

```html
<!DOCTYPE html>
<html lang="en">
<head>
<meta charset="utf-8">
<title>Polystyrene Recycling Material Flow</title>
<link rel="stylesheet" href="https://fonts.googleapis.com/css2?family=Montserrat:wght@400;500;600;700;800&display=swap">
<style>
  :root {
    --orange: #f6a01a;
    --orange-flow: #f3a33a;
    --brown: #5b2a17;
    --cream: #fff6e6;
    --cream-line: #f3c98a;
    --gold: #bf8c0c;
    --band: #f1e7e9;
    --olive: #9aad1f;
    --steel: #5a87a6;
    --green-tint: #eef5e2;
    --green-line: #a9c47a;
    --blue-tint: #e7eff7;
    --blue-line: #a3b9cf;
    --ink: #1c2738;
    --muted: #4a4f57;
    --blue-note: #5a7a96;
    --white: #ffffff;
  }
  * { box-sizing: border-box; margin: 0; padding: 0; }
  html, body { width: 1200px; height: 1200px; overflow: hidden; background: var(--white); }
  body { font-family: "Montserrat", Arial, sans-serif; }
  .canvas {
    position: relative; width: 980px; height: 980px;
    transform: scale(1.22449); transform-origin: 0 0;
  }
  .flow-lines { position: absolute; inset: 0; width: 980px; height: 980px; }
  .node { position: absolute; display: flex; align-items: center; justify-content: center; text-align: center; }

  .title-block {
    left: 697px; top: 200px; width: 225px; height: 86px; background: var(--orange);
    flex-direction: column; color: var(--white); text-transform: uppercase; line-height: 1;
  }
  .title-block .t1 { font-size: 19px; font-weight: 600; letter-spacing: .3px; }
  .title-block .t2 { font-size: 30px; font-weight: 800; margin: 2px 0; }
  .title-block .t3 { font-size: 19px; font-weight: 600; letter-spacing: .3px; }

  .sources-bar { left: 102px; top: 234px; width: 33px; height: 162px; background: var(--brown); }
  .sources-bar span {
    transform: rotate(-90deg); white-space: nowrap; color: var(--white);
    font-size: 11px; font-weight: 700; letter-spacing: .4px;
  }
  .source {
    left: 139px; width: 164px; height: 40px; background: var(--orange); justify-content: flex-start;
    padding-left: 10px; color: var(--white); font-size: 11.5px; font-weight: 700;
  }
  .source-note {
    left: 303px; width: 112px; height: 40px; background: var(--cream); border: 1px solid var(--cream-line);
    flex-direction: column; align-items: flex-start; padding-left: 6px; font-size: 10px; color: var(--muted); line-height: 1.35;
  }

  .collection-ring {
    left: 461px; top: 259px; width: 114px; height: 114px; border-radius: 50%;
    border: 1px solid var(--gold); background: var(--white);
  }
  .collection-ring span {
    width: 104px; height: 104px; border-radius: 50%; background: var(--gold);
    display: flex; align-items: center; justify-content: center;
    color: var(--white); font-size: 13px; font-weight: 700;
  }

  .process-band { position: absolute; left: 102px; top: 430px; width: 795px; height: 89px; background: var(--band); }
  .process { height: 38px; width: 164px; color: var(--white); font-size: 15px; font-weight: 700; }
  .process-compaction { left: 201px; top: 456px; background: var(--olive); }
  .process-regrind { left: 622px; top: 455px; background: var(--steel); }
  .process-note { position: absolute; font-size: 10.5px; color: var(--muted); line-height: 13.5px; }
  .process-note.left { right: 784px; top: 455px; text-align: right; }
  .process-note.left i { color: var(--olive); font-style: normal; }
  .process-note.right { left: 793px; top: 469px; }

  .step { color: var(--ink); font-size: 11.5px; font-weight: 700; line-height: 1.3; }
  .step.green { background: var(--green-tint); border: 1px solid var(--green-line); }
  .step.blue { background: var(--blue-tint); border: 1px solid var(--blue-line); }
  .step.small { font-size: 9.5px; }
  .step-notes { position: absolute; left: 758px; top: 571px; font-size: 10.5px; color: var(--blue-note); line-height: 14px; }
</style>
</head>
<body>
<main class="canvas">
  <div class="process-band"></div>

  <svg class="flow-lines" viewBox="0 0 980 980" aria-hidden="true">
    <defs>
      <path id="head" d="M-5 -5 L5 0 L-5 5 Z" fill="#f3a33a"/>
    </defs>
    <g fill="none" stroke="#f3a33a" stroke-width="2.2" stroke-dasharray="2 3">
      <polyline points="341,676 341,768 58,768 58,200 516,200 516,232"/>
      <line x1="303" y1="316" x2="461" y2="316"/>
      <line x1="390" y1="274" x2="390" y2="357"/>
      <line x1="516" y1="373" x2="516" y2="476"/>
      <line x1="365" y1="476" x2="622" y2="476"/>
      <line x1="224" y1="494" x2="224" y2="548"/>
      <line x1="341" y1="494" x2="341" y2="548"/>
      <line x1="224" y1="600" x2="224" y2="624"/>
      <line x1="224" y1="676" x2="224" y2="696"/>
      <line x1="361" y1="600" x2="361" y2="624"/>
      <line x1="688" y1="493" x2="688" y2="566"/>
      <polyline points="688,680 688,768 922,768 922,316 575,316"/>
    </g>
    <use href="#head" transform="translate(298,200)"/>
    <use href="#head" transform="translate(516,232) rotate(90)"/>
    <use href="#head" transform="translate(58,612) rotate(-90)"/>
    <use href="#head" transform="translate(58,373) rotate(-90)"/>
    <use href="#head" transform="translate(178,768) rotate(180)"/>
    <use href="#head" transform="translate(341,722) rotate(90)"/>
    <use href="#head" transform="translate(433,316)"/>
    <use href="#head" transform="translate(390,291) rotate(90)"/>
    <use href="#head" transform="translate(390,342) rotate(-90)"/>
    <use href="#head" transform="translate(516,401) rotate(90)"/>
    <use href="#head" transform="translate(447,476) rotate(180)"/>
    <use href="#head" transform="translate(566,476)"/>
    <use href="#head" transform="translate(224,530) rotate(90)"/>
    <use href="#head" transform="translate(341,530) rotate(90)"/>
    <use href="#head" transform="translate(224,614) rotate(90)"/>
    <use href="#head" transform="translate(224,688) rotate(90)"/>
    <use href="#head" transform="translate(361,614) rotate(90)"/>
    <use href="#head" transform="translate(688,532) rotate(90)"/>
    <use href="#head" transform="translate(688,722) rotate(90)"/>
    <use href="#head" transform="translate(802,768)"/>
    <use href="#head" transform="translate(922,612) rotate(-90)"/>
    <use href="#head" transform="translate(922,378) rotate(-90)"/>
    <use href="#head" transform="translate(773,316) rotate(180)"/>
  </svg>

  <header class="node title-block">
    <span class="t1">Polystyrene</span>
    <span class="t2">Recycling</span>
    <span class="t3">Material Flow</span>
  </header>

  <div class="node sources-bar"><span>EPS WASTE SOURCES</span></div>
  <div class="node source" style="top:234px">MUNICIPAL WASTE</div>
  <div class="node source" style="top:296px">MANUFACTURING WASTE</div>
  <div class="node source" style="top:357px">COMMERCIAL WASTE</div>
  <div class="node source-note" style="top:234px"><span>• Curbside Collection</span><span>• Drop Off Centers</span></div>
  <div class="node source-note" style="top:357px"><span>• Back Hauling</span><span>• Localized Delivery</span></div>

  <div class="node collection-ring"><span>COLLECTION</span></div>

  <p class="process-note left">Extruded Ingot <i>•</i><br>Hydrolic <i>•</i><br>Compression <i>•</i></p>
  <div class="node process process-compaction">COMPACTION</div>
  <div class="node process process-regrind">REGRIND</div>
  <p class="process-note right">• Molder Facilities</p>

  <div class="node step green" style="left:102px;top:548px;width:148px;height:52px">Recycled Content<br>EPS RESIN</div>
  <div class="node step green" style="left:102px;top:624px;width:148px;height:52px">RE-PELLETIZED<br>with Blowing Agent</div>
  <div class="node step green small" style="left:102px;top:696px;width:148px;height:52px">EXPANDED POLYSTYRENE<br>Packaging &amp; Building<br>Products ≤50%</div>
  <div class="node step green" style="left:287px;top:548px;width:149px;height:52px">EXTRUDED<br>Rigid S Pellet</div>
  <div class="node step green" style="left:287px;top:624px;width:149px;height:52px">END MARKET<br>Applications</div>

  <div class="node step blue" style="left:620px;top:566px;width:131px;height:36px">SHREDDING</div>
  <div class="node step blue" style="left:620px;top:625px;width:131px;height:55px">Recycled Content<br>PACKAGING ≤15%</div>
  <p class="step-notes">• Homogenization<br>• Mixing for Consistency</p>
</main>
</body>
</html>
```